Design für Zeitungsanzeige hochwertige Betten
Zielgruppe
Ruhepunkt Sana verkauft hochwertige Bettsystem für schmerzfreies Liegen und Schlafen. Die Kunden (40+) kommen in das Geschäft, weil sie Rückenschmerzen haben und nicht gut schlafen können. Dort werden Sie individuell beraten. Ruhepunkt Sana hat einen Expertenstatus rum um das Thema Liegen und Schlafen, da Sie maßgeschneiderte Matratzen mit Hilfe von Liegedruckmessung anbieten. Die Produkte sind frei von Chemie und Pestiziden, was positiv zum guten Schlaf beiträgt. Somit sind die Produkte auch sehr hochwertig, aber auch kostspielig.
Aufgabenstellung
Gern einmal auf die Seite:
http://www.ruhepunkt-lindenau.de/traumbetten/
http://www.ruhepunkt-sana.com/betten/
-Vorher / nachher Bilder sind sehr effektvoll
-Unbedingt in die Anzeigen nehmen: Adresse- Logo Firma, "Ergonomische Betten" soll mit auf der Anzeige sein und vom Stil ähnlich zu der Schuhanzeige aufgebaut sein.
- gerne auch Unten mit GUTSCHEIN und einer Schere: Kostenlose Liegedruck-Messung
- Zielgruppe 40+
- ein Bett im Hintergrund würde sinnmachen, wenn eine Person davor steht und sich den Rücken hält.
- In der Art wollen wir auch die Anzeige haben. Gut wäre wenn eine ältere Dame zusehen ist, die genau der Zielgruppe entspricht.
Allgemeines:
- Die hohe Qualität der Produkte soll im Vordergrund stehen und die richtige Zielgruppe mit dem passenden Kleingeld ansprechen.
- Das Ruhepunkt Sana Logo muss zusehen sein und auffallen, da dieses sich bei den Menschen einprägen soll.
- Kunden sollen aufgefordert werden zu Ruhepunkt Sana ins Geschäft zu kommen und Ruhepunkt Sana als Experte und Berater soll im Vordergrund stehen.
- Adresse mit Ort muss zusehen sein.
Eine Zeitungsanzeige 4-farbig
Maße: querformat 5*9 cm (und vllt hochformat 4,5*14cm)

```html
<!DOCTYPE html>
<html lang="de">
<head>
<meta charset="utf-8">
<title>Ruhepunkt Sana – Anzeigenvarianten</title>
<link href="https://fonts.googleapis.com/css2?family=Crimson+Text&family=Source+Sans+3:wght@400;600;700&family=Caveat:wght@600&display=swap" rel="stylesheet">
<style>
  :root {
    --maroon: #6d1a32;
    --maroon-text: #7a1d2e;
    --green: #5cc21f;
    --ink: #222222;
    --frame: #555555;
    --paper: #ffffff;
    --photo-light: #f6f6f6;
    --photo-mid: #e3e3e3;
    --step-grey: #8a9a9a;
  }
  * { box-sizing: border-box; margin: 0; padding: 0; }
  html, body { width: 1200px; height: 801px; overflow: hidden; background: var(--paper); }
  body { position: relative; font-family: "Source Sans 3", Arial, sans-serif; color: var(--ink); }

  .variant-label {
    position: absolute;
    font-family: "Crimson Text", Georgia, serif;
    font-size: 21px;
    color: #111;
    transform: translateX(-50%);
  }

  .ad {
    position: absolute;
    width: 460px;
    height: 255px;
    border: 1px solid var(--frame);
    background: linear-gradient(180deg, #fafafa 0%, #f2f2f2 100%);
    overflow: hidden;
  }
  .ad > * { position: absolute; }

  .ad__photo {
    top: 0; bottom: 0;
    background: linear-gradient(90deg, var(--photo-mid) 0%, var(--photo-light) 100%);
  }
  .ad__photo--right { background: linear-gradient(270deg, var(--photo-mid) 0%, var(--photo-light) 100%); }

  .ad__questions {
    font-weight: 700;
    color: var(--maroon-text);
    letter-spacing: -0.2px;
  }
  .ad__dots {
    height: 0;
    border-top: 2px dotted var(--green);
  }
  .ad__change {
    font-weight: 700;
    text-align: right;
    color: var(--ink);
    letter-spacing: -0.2px;
  }
  .ad__intro {
    font-weight: 700;
    letter-spacing: -0.2px;
  }
  .brand {
    display: flex;
    align-items: center;
    gap: 6px;
    font-weight: 700;
    color: var(--maroon);
    white-space: nowrap;
  }
  .brand__dot {
    width: 12px; height: 12px;
    border-radius: 50%;
    background: var(--green);
  }
  .ad__address { line-height: 1.3; }
  .ad__phone { font-weight: 700; }
  .ad__phone--accent { color: var(--maroon); }

  .steps {
    background: var(--step-grey);
    opacity: 0.35;
    border-radius: 6px;
  }

  .badge {
    border-radius: 50%;
    background: var(--maroon);
    color: #fff;
    display: flex;
    flex-direction: column;
    align-items: center;
    justify-content: center;
    transform: rotate(-12deg);
  }
  .badge__claim {
    font-family: "Caveat", cursive;
    font-weight: 600;
    line-height: 1;
    text-align: center;
    margin-bottom: 3px;
  }
  .badge__list { list-style: none; }
  .badge__list li {
    display: flex; align-items: center; gap: 3px;
    line-height: 1.15;
  }
  .badge__tick { flex: none; }

  .voucher-corner { right: 0; bottom: 0; }
  .voucher-corner__text {
    color: #fff;
    font-weight: 600;
    font-size: 12px;
    line-height: 1.15;
    text-align: center;
    transform: rotate(-45deg);
    width: 120px;
  }

  .voucher-band {
    left: 0; right: 0; bottom: 0;
    height: 30px;
    background: var(--maroon);
    color: #fff;
    font-size: 16px;
    font-weight: 600;
    display: flex; align-items: center; justify-content: center;
  }
</style>
</head>
<body>

<!-- Variante 1 -->
<div class="variant-label" style="left:317px; top:60px;">Variante 1</div>
<div class="ad" style="left:95px; top:106px;">
  <div class="ad__photo" role="img" aria-label="Foto: ältere Dame hält sich den Rücken, Bett im Hintergrund" style="left:0; width:135px;"></div>
  <div class="ad__questions" style="left:115px; top:16px; font-size:16px; line-height:21.6px;">Unausgeschlafen?<br>Rückenschmerzen?<br>Steifer Hals?</div>
  <div class="ad__dots" style="left:268px; top:37px; width:60px;"></div>
  <div class="ad__change" style="right:24px; top:18px; font-size:16px; line-height:22px;">Zeit für eine<br>Veränderung.</div>
  <div class="steps" role="img" aria-label="Fußspuren" style="left:404px; top:62px; width:30px; height:58px;"></div>
  <div class="ad__intro" style="left:213px; top:96px; font-size:15px;">Ergonomische Betten bei:</div>
  <div class="brand" style="left:213px; top:121px; font-size:24px;"><span>Ruhepunkt Sana</span><span class="brand__dot"></span></div>
  <div class="ad__address" style="left:211px; top:155px; font-size:16px; line-height:20.5px;">Ruhepunkt Sana<br>Lindenweg 8<br>23845 Lindenau<br><span class="ad__phone">04321 55 18 90</span></div>
  <div class="badge" style="left:116px; top:121px; width:86px; height:86px;">
    <div class="badge__claim" style="font-size:13px;">Wir nehmen<br>uns Zeit!</div>
    <ul class="badge__list" style="font-size:8.5px;">
      <li><svg class="badge__tick" width="8" height="8" viewBox="0 0 10 10"><circle cx="5" cy="5" r="5" fill="#5cc21f"/><path d="M2.5 5.2l1.7 1.7 3.4-3.6" stroke="#fff" stroke-width="1.5" fill="none"/></svg>Vorbeikommen</li>
      <li><svg class="badge__tick" width="8" height="8" viewBox="0 0 10 10"><circle cx="5" cy="5" r="5" fill="#5cc21f"/><path d="M2.5 5.2l1.7 1.7 3.4-3.6" stroke="#fff" stroke-width="1.5" fill="none"/></svg>Beraten lassen</li>
      <li><svg class="badge__tick" width="8" height="8" viewBox="0 0 10 10"><circle cx="5" cy="5" r="5" fill="#5cc21f"/><path d="M2.5 5.2l1.7 1.7 3.4-3.6" stroke="#fff" stroke-width="1.5" fill="none"/></svg>Probeliegen</li>
    </ul>
  </div>
  <svg class="voucher-corner" width="142" height="141" viewBox="0 0 142 141" aria-hidden="true"><polygon points="142,0 142,141 0,141" fill="#6d1a32"/></svg>
  <div class="voucher-corner__text" style="left:337px; top:184px;">GUTSCHEIN<br>Kostenlose<br>Liegedruck-<br>Messung</div>
</div>

<!-- Variante 2 -->
<div class="variant-label" style="left:876px; top:60px;">Variante 2</div>
<div class="ad" style="left:649px; top:106px;">
  <div class="ad__photo" role="img" aria-label="Foto: ältere Dame hält sich den Rücken, Bett im Hintergrund" style="left:0; width:118px; bottom:30px;"></div>
  <div class="ad__questions" style="left:125px; top:12px; font-size:14.5px; line-height:20px;">Unausgeschlafen?<br>Rückenschmerzen?<br>Steifer Hals?</div>
  <div class="ad__dots" style="left:265px; top:35px; width:74px;"></div>
  <div class="ad__change" style="right:23px; top:16px; font-size:14.5px; line-height:20px;">Zeit für eine<br>Veränderung.</div>
  <div class="steps" role="img" aria-label="Fußspuren" style="left:324px; top:62px; width:36px; height:60px;"></div>
  <div class="ad__intro" style="left:153px; top:81px; font-size:14.5px;">Ergonomische Betten bei:</div>
  <div class="brand" style="left:150px; top:105px; font-size:24px;"><span>Ruhepunkt Sana</span><span class="brand__dot"></span></div>
  <div class="ad__address" style="left:150px; top:140px; font-size:15.5px; line-height:20px;">Ruhepunkt Sana<br>Lindenweg 8<br>23845 Lindenau<br><span class="ad__phone ad__phone--accent">04321 55 18 90</span></div>
  <div class="badge" style="left:346px; top:112px; width:104px; height:104px;">
    <div class="badge__claim" style="font-size:15px;">Wir nehmen<br>uns Zeit!</div>
    <ul class="badge__list" style="font-size:10px;">
      <li><svg class="badge__tick" width="9" height="9" viewBox="0 0 10 10"><circle cx="5" cy="5" r="5" fill="#5cc21f"/><path d="M2.5 5.2l1.7 1.7 3.4-3.6" stroke="#fff" stroke-width="1.5" fill="none"/></svg>Vorbeikommen</li>
      <li><svg class="badge__tick" width="9" height="9" viewBox="0 0 10 10"><circle cx="5" cy="5" r="5" fill="#5cc21f"/><path d="M2.5 5.2l1.7 1.7 3.4-3.6" stroke="#fff" stroke-width="1.5" fill="none"/></svg>Beraten lassen</li>
      <li><svg class="badge__tick" width="9" height="9" viewBox="0 0 10 10"><circle cx="5" cy="5" r="5" fill="#5cc21f"/><path d="M2.5 5.2l1.7 1.7 3.4-3.6" stroke="#fff" stroke-width="1.5" fill="none"/></svg>Probeliegen</li>
    </ul>
  </div>
  <div class="voucher-band">IHR GUTSCHEIN für eine kostenlose Liegedruck-Messung</div>
</div>

<!-- Variante 3 -->
<div class="variant-label" style="left:572px; top:387px;">Variante 3</div>
<div class="ad" style="left:356px; top:430px;">
  <div class="ad__photo ad__photo--right" role="img" aria-label="Foto: ältere Dame hält sich den Rücken, Bett im Hintergrund" style="right:0; width:122px; bottom:30px;"></div>
  <div class="ad__questions" style="left:21px; top:14px; font-size:14.5px; line-height:20px;">Unausgeschlafen?<br>Rückenschmerzen?<br>Steifer Hals?</div>
  <div class="ad__dots" style="left:161px; top:36px; width:68px;"></div>
  <div class="ad__change" style="left:235px; width:100px; top:18px; font-size:14.5px; line-height:20px;">Zeit für eine<br>Veränderung.</div>
  <div class="ad__intro" style="left:130px; top:79px; font-size:14.5px;">Ergonomische Betten bei:</div>
  <div class="brand" style="left:130px; top:104px; font-size:24px;"><span>Ruhepunkt Sana</span><span class="brand__dot"></span></div>
  <div class="ad__address" style="left:130px; top:137px; font-size:15.5px; line-height:20px;">Ruhepunkt Sana<br>Lindenweg 8<br>23845 Lindenau<br><span class="ad__phone ad__phone--accent">04321 55 18 90</span></div>
  <div class="steps" role="img" aria-label="Fußspuren" style="left:258px; top:158px; width:64px; height:50px;"></div>
  <div class="badge" style="left:16px; top:110px; width:104px; height:104px;">
    <div class="badge__claim" style="font-size:15px;">Wir nehmen<br>uns Zeit!</div>
    <ul class="badge__list" style="font-size:10px;">
      <li><svg class="badge__tick" width="9" height="9" viewBox="0 0 10 10"><circle cx="5" cy="5" r="5" fill="#5cc21f"/><path d="M2.5 5.2l1.7 1.7 3.4-3.6" stroke="#fff" stroke-width="1.5" fill="none"/></svg>Vorbeikommen</li>
      <li><svg class="badge__tick" width="9" height="9" viewBox="0 0 10 10"><circle cx="5" cy="5" r="5" fill="#5cc21f"/><path d="M2.5 5.2l1.7 1.7 3.4-3.6" stroke="#fff" stroke-width="1.5" fill="none"/></svg>Beraten lassen</li>
      <li><svg class="badge__tick" width="9" height="9" viewBox="0 0 10 10"><circle cx="5" cy="5" r="5" fill="#5cc21f"/><path d="M2.5 5.2l1.7 1.7 3.4-3.6" stroke="#fff" stroke-width="1.5" fill="none"/></svg>Probeliegen</li>
    </ul>
  </div>
  <div class="voucher-band">IHR GUTSCHEIN für eine kostenlose Liegedruck-Messung</div>
</div>

</body>
</html>
```